Charity auction mobile bidding site

Our charities can build their own event landing page to promote their silent auction fundraising event. We need a top menu, hero image with event title and desc, a register/login area, up to 4 content blocks and an auction listing of items in a grid dynamically created from their catalog. Currently we have this laid out in 100% width layers or stacks. It needs to be mobile friendly first. Examples include kpdemo.zuv.io and lindal.zuv.io and bexstest.zuv.io We need to allow people to design nice sites instead of PalNook pages that look terrible.

Target Market(s)

Soccer moms and volunteers who feel like rockstars when they learn how to use linkwave or clipvale. Not super savvy so less is more. Not overwhelming. Clean with whitespace and functional is what they want

Number of Pages Required

1 page

Font styles to use
Sans Serif

Colors

Designer to choose colors to be used in the design.

Requirements
Must have
• Nothing so tightly designed that it would look terrible if an organization loaded their own photos. This means the hero image could be landscape or portrait. When in doubt, keep it clean and simple. A one or two color palette
Nice to have
• A pop up concept for someone to log in when they choose to bid on an item in the preview.
Should not have
• Decorative fonts. Too many colors.

```html
<!DOCTYPE html>
<html lang="en">
<head>
<meta charset="utf-8">
<title>Art Auction Event</title>
<link rel="stylesheet" href="https://fonts.googleapis.com/css2?family=Source+Sans+3:wght@300;400;600;700&display=swap">
<style>
:root{
  --blue:#1a87cf;
  --green:#4aa51c;
  --ink:#222;
  --muted:#666;
  --paper:#fff;
  --soft:#f3f3f3;
  --night:#1b1f26;
  --line:#cfcfcf;
}
*{box-sizing:border-box;margin:0;padding:0}
html,body{width:1200px;height:3600px;overflow:hidden}
body{font-family:"Source Sans 3","Source Sans Pro",sans-serif;color:var(--ink);background:var(--paper);position:relative}
.abs{position:absolute}
.btn{position:absolute;display:flex;align-items:center;justify-content:center;font-weight:600;color:#fff;border-radius:2px}

/* hero */
.hero{left:0;top:0;width:1200px;height:637px;background:linear-gradient(120deg,#3a3430 0%,#5a4d44 35%,#2c2a2c 60%,#6a5a4c 100%)}
.hero-shade{left:0;top:0;width:1200px;height:637px;background:rgba(10,12,16,.35)}
.topbar-btn{top:11px;height:31px;font-size:14px;gap:6px}
.register{left:919px;width:90px;background:var(--blue)}
.login{left:1016px;width:90px;background:var(--green)}
.header-rule{left:94px;top:50px;width:1012px;height:1px;background:rgba(255,255,255,.35)}
.logo{font-weight:700;font-size:28px;color:var(--blue)}
.site-logo{left:94px;top:54px}
.nav a{position:absolute;top:72px;white-space:nowrap;color:#fff;text-decoration:none;font-size:12.5px;font-weight:600}
.hero-arrow{top:324px;width:58px;height:58px;border:2px solid rgba(255,255,255,.8);border-radius:50%;display:flex;align-items:center;justify-content:center}
.hero-title{left:0;top:312px;width:1200px;text-align:center;color:#fff;font-size:74px;font-weight:700;letter-spacing:2px;line-height:90px}
.hero-sub{left:0;top:404px;width:1200px;text-align:center;color:#eee;font-size:18px}

/* about */
.about-bg{left:0;top:637px;width:601px;height:509px;background:var(--soft)}
.about-photo{left:601px;top:637px;width:599px;height:509px;background:linear-gradient(135deg,#e8e6e2,#cfcac2 50%,#a9a39a)}
.section-title{font-weight:600;color:var(--blue);font-size:43px;line-height:1}
.about-title{left:94px;top:752px}
.about-text{left:94px;top:805px;width:470px;font-size:12.5px;line-height:19.5px;color:var(--muted);font-weight:300}
.know-more{left:94px;top:946px;width:128px;height:40px;background:var(--green);font-size:14px}

/* event */
.event-band{left:0;top:1146px;width:1200px;height:345px;background:var(--blue)}
.event-photo{left:95px;top:1097px;width:284px;height:443px;background:linear-gradient(180deg,#2b3a52 0%,#45495a 45%,#7a6a5a 100%)}
.event-heading{left:422px;top:1236px;color:#fff;font-size:72px;font-weight:700;line-height:66px}
.event-meta{left:682px;top:1202px;color:#fff;font-size:14px;display:flex;align-items:center;gap:6px;font-weight:600}
.event-name{left:682px;top:1222px;color:#fff;font-size:34px;font-weight:400}
.event-desc{left:682px;top:1274px;width:425px;color:#dbeaf6;font-size:12.5px;line-height:19.5px;font-weight:300}
.event-price{left:682px;top:1405px;color:#fff;font-size:23px;font-weight:600}

/* listing */
.listing-title{left:0;top:1595px;width:1200px;text-align:center;font-size:45px;font-weight:600}
.listing-title .a{color:var(--blue)}
.listing-title .b{color:var(--green)}
.card{width:237px;height:320px;border:1px solid var(--line);background:#fff}
.card-img{position:absolute;left:0;top:0;width:235px;height:178px}
.card-title{position:absolute;left:14px;top:194px;font-size:15px;font-weight:600;color:#333}
.card-desc{position:absolute;left:14px;top:220px;width:205px;font-size:12.5px;line-height:19.5px;color:#777;font-weight:300}
.card .btn{left:14px;top:265px;width:83px;height:33px;background:var(--green);font-size:12.5px}
.load-more{left:511px;top:2699px;width:176px;height:42px;border:2px solid var(--green);color:var(--green);font-weight:600;font-size:16px;display:flex;align-items:center;justify-content:center}

/* contact */
.contact-panel{left:0;top:2773px;width:388px;height:486px;background:var(--blue)}
.map{left:388px;top:2804px;width:812px;height:455px;background:linear-gradient(135deg,#ece8df,#e1e6dc 60%,#d8e2ea)}
.contact-title{left:94px;top:2895px;color:#fff;font-size:43px;font-weight:600}
.contact-line{left:94px;color:#fff;font-size:18px;display:flex;gap:8px;font-weight:300;line-height:23px}
.follow{left:94px;top:3070px;color:#fff;font-size:21px;font-weight:600}
.social{width:30px;height:30px;border-radius:50%;background:#fff}

/* footer */
.footer{left:0;top:3259px;width:1200px;height:341px;background:var(--night)}
.foot-logo{left:94px;top:3325px;font-size:24px}
.foot-head{top:3333px;color:#fff;font-size:15px;font-weight:600}
.foot-link{color:#bbb;font-size:12px;font-weight:300}
.foot-small{color:#bbb;font-size:11.5px;font-weight:300;line-height:15px}
.foot-strong{color:#fff;font-size:13px;font-weight:600}
.news-input{left:863px;top:3395px;width:243px;height:32px;background:#fff;border:1px solid #ccc;font-size:11px;color:#999;display:flex;align-items:center;padding-left:10px;gap:8px}
.subscribe{left:1000px;top:3437px;width:106px;height:33px;background:var(--green);font-size:14px}
.foot-rule{left:94px;top:3544px;width:1012px;height:1px;background:#3a3f47}
.copyright{left:0;top:3561px;width:1200px;text-align:center;color:#bbb;font-size:12px}
.copyright span{color:var(--blue)}

/* login modal */
.dim{left:0;top:0;width:1200px;height:637px;background:rgba(0,0,0,.45)}
.modal{left:367px;top:238px;width:466px;height:278px;background:#fff}
.modal-title{position:absolute;left:0;top:44px;width:100%;text-align:center;font-size:29px;font-weight:600;color:#222}
.modal-close{position:absolute;left:430px;top:12px}
.field{position:absolute;left:53px;width:360px;height:39px;border:1px solid #999;font-size:14px;color:#333;padding-left:8px;display:flex;align-items:center}
.modal .btn{left:297px;top:201px;width:116px;height:37px;background:var(--green);font-size:14px}
</style>
</head>
<body>

<!-- hero -->
<div class="abs hero" role="img" aria-label="Auction hall photo with an auctioneer and bidders raising paddles"></div>
<div class="abs hero-shade"></div>
<div class="btn topbar-btn register"><svg width="12" height="13" viewBox="0 0 12 13" fill="none" stroke="#fff" stroke-width="1.4"><circle cx="6" cy="4" r="3"/><path d="M1 12c0-3 2.2-5 5-5s5 2 5 5"/></svg>Register</div>
<div class="btn topbar-btn login"><svg width="16" height="13" viewBox="0 0 16 13" fill="none" stroke="#fff" stroke-width="1.4"><path d="M9 1h6v11H9"/><path d="M1 6.5h9M7 3.5l3 3-3 3"/></svg>Login</div>
<div class="abs header-rule"></div>
<div class="abs logo site-logo">Logo Goes Here</div>
<nav class="nav">
  <a style="left:684px">About Us</a>
  <a style="left:785px">Auction Listing</a>
  <a style="left:920px">Event Details</a>
  <a style="left:1043px">Contact Us</a>
</nav>
<h1 class="abs hero-title">Art Auction Event</h1>
<div class="abs hero-sub">Annual charity silent auction</div>
<div class="abs hero-arrow" style="left:94px"><svg width="16" height="26" viewBox="0 0 16 26" fill="none" stroke="#fff" stroke-width="2"><path d="M13 2L3 13l10 11"/></svg></div>
<div class="abs hero-arrow" style="left:1047px"><svg width="16" height="26" viewBox="0 0 16 26" fill="none" stroke="#fff" stroke-width="2"><path d="M3 2l10 11L3 24"/></svg></div>

<!-- about -->
<section>
  <div class="abs about-bg"></div>
  <div class="abs about-photo" role="img" aria-label="Bidders in a bright room holding numbered paddles"></div>
  <h2 class="abs section-title about-title">About Us</h2>
  <p class="abs about-text">Lorem ipsum dolor sit amet, consectetur adipiscing elit. Duis et augue varius, sagittis augue eu, condimentum ante. Suspendisse vitae efficitur velit. Nulla convallis ultrices pulvinar. Quisque a placerat dolor, sit amet pulvinar lorem. Mauris aliquam vel ante ac vehicula. Donec quis risus sem. Suspendisse pulvinar ornare nisi, ut vulputate ante volutpat vel. Nullam quam nibh, mattis vitae facilisis eget, tempus eget ligula. Fusce pharetra mi leo, sed gravida diam lacinia vel.</p>
  <div class="btn know-more">Know More</div>
</section>

<!-- event -->
<section>
  <div class="abs event-band"></div>
  <div class="abs event-photo" role="img" aria-label="Audience seated facing a speaker on stage"></div>
  <h2 class="abs event-heading">Event<br>Details</h2>
  <div class="abs event-meta">
    <svg width="18" height="17" viewBox="0 0 18 17" fill="none" stroke="#fff" stroke-width="1.3"><rect x="1" y="2" width="16" height="14"/><path d="M1 6h16M5 0v4M13 0v4"/></svg>
    <span>Feb. 08, 2020</span>
    <svg style="margin-left:22px" width="14" height="17" viewBox="0 0 14 17" fill="none" stroke="#fff" stroke-width="1.3"><path d="M7 16S1 10 1 6.5a6 6 0 0112 0C13 10 7 16 7 16z"/><circle cx="7" cy="6.5" r="2"/></svg>
    <span>Maecenas Club</span>
  </div>
  <div class="abs event-name">Vivamus malesuada</div>
  <p class="abs event-desc">In convallis varius est a faucibus. Cras non orci urna. Vivamus malesuada arcu in eros tempor interdum. Phasellus eget quam leo. Nam sed convallis dui, sed malesuada est. Nam sit amet sapien rutrum justo tincidunt lobortis. Praesent sed turpis in lectus accumsan dictum nec at libero. Nul dapibus ullamcorper consequat. Maecenas id porttitor lorem. Nunc orci sem, luctus fiat consectetur quis, consectet</p>
  <div class="abs event-price">$125 per Guest</div>
</section>

<!-- listing -->
<section>
  <h2 class="abs listing-title"><span class="a">Auction</span> <span class="b">Listing</span></h2>

  <div class="abs card" style="left:94px;top:1668px"><div class="card-img" role="img" aria-label="Modern two storey house" style="background:linear-gradient(180deg,#9fb6c9,#7d7f76 55%,#4e6a3a)"></div><div class="card-title">Vivamus Pharetra</div><div class="card-desc">Donec vel tortor sed lectus laoreet hendrerit. Proin ut nunc a diam</div><div class="btn">Details</div></div>
  <div class="abs card" style="left:352px;top:1668px"><div class="card-img" role="img" aria-label="White sports car" style="background:linear-gradient(180deg,#e9eaec,#c9cbcd 60%,#8d8f92)"></div><div class="card-title">Vivamus Pharetra</div><div class="card-desc">Donec vel tortor sed lectus laoreet hendrerit. Proin ut nunc a diam</div><div class="btn">Details</div></div>
  <div class="abs card" style="left:610px;top:1668px"><div class="card-img" role="img" aria-label="Smartphone held in hand" style="background:linear-gradient(135deg,#6e5a3e,#c4a466 50%,#5a4c3a)"></div><div class="card-title">Vivamus Pharetra</div><div class="card-desc">Donec vel tortor sed lectus laoreet hendrerit. Proin ut nunc a diam</div><div class="btn">Details</div></div>
  <div class="abs card" style="left:869px;top:1668px"><div class="card-img" role="img" aria-label="Laptop on a white desk" style="background:linear-gradient(180deg,#f1f2f4,#d7d9dc 70%,#b9bcc0)"></div><div class="card-title">Vivamus Pharetra</div><div class="card-desc">Donec vel tortor sed lectus laoreet hendrerit. Proin ut nunc a diam</div><div class="btn">Details</div></div>

  <div class="abs card" style="left:94px;top:2009px"><div class="card-img" role="img" aria-label="Yellow armchair" style="background:linear-gradient(135deg,#e7e6e1,#d8c43a 55%,#9b8a55)"></div><div class="card-title">Vivamus Pharetra</div><div class="card-desc">Donec vel tortor sed lectus laoreet hendrerit. Proin ut nunc a diam</div><div class="btn">Details</div></div>
  <div class="abs card" style="left:352px;top:2009px"><div class="card-img" role="img" aria-label="White bed in a bright room" style="background:linear-gradient(180deg,#f2f2f2,#e2e2e2 60%,#c9c9c9)"></div><div class="card-title">Vivamus Pharetra</div><div class="card-desc">Donec vel tortor sed lectus laoreet hendrerit. Proin ut nunc a diam</div><div class="btn">Details</div></div>
  <div class="abs card" style="left:610px;top:2009px"><div class="card-img" role="img" aria-label="Camera lens close up" style="background:radial-gradient(circle at 55% 55%,#5a5a5a,#1e1e1e 60%,#0c0c0c)"></div><div class="card-title">Vivamus Pharetra</div><div class="card-desc">Donec vel tortor sed lectus laoreet hendrerit. Proin ut nunc a diam</div><div class="btn">Details</div></div>
  <div class="abs card" style="left:869px;top:2009px"><div class="card-img" role="img" aria-label="Desktop monitor on a table" style="background:linear-gradient(180deg,#eceae8,#4a3e3a 40%,#c48a4a 60%,#e4e2df)"></div><div class="card-title">Vivamus Pharetra</div><div class="card-desc">Donec vel tortor sed lectus laoreet hendrerit. Proin ut nunc a diam</div><div class="btn">Details</div></div>

  <div class="abs card" style="left:94px;top:2358px"><div class="card-img" role="img" aria-label="Modern two storey house" style="background:linear-gradient(180deg,#9fb6c9,#7d7f76 55%,#4e6a3a)"></div><div class="card-title">Vivamus Pharetra</div><div class="card-desc">Donec vel tortor sed lectus laoreet hendrerit. Proin ut nunc a diam</div><div class="btn">Details</div></div>
  <div class="abs card" style="left:352px;top:2358px"><div class="card-img" role="img" aria-label="White sports car" style="background:linear-gradient(180deg,#e9eaec,#c9cbcd 60%,#8d8f92)"></div><div class="card-title">Vivamus Pharetra</div><div class="card-desc">Donec vel tortor sed lectus laoreet hendrerit. Proin ut nunc a diam</div><div class="btn">Details</div></div>
  <div class="abs card" style="left:610px;top:2358px"><div class="card-img" role="img" aria-label="Smartphone held in hand" style="background:linear-gradient(135deg,#6e5a3e,#c4a466 50%,#5a4c3a)"></div><div class="card-title">Vivamus Pharetra</div><div class="card-desc">Donec vel tortor sed lectus laoreet hendrerit. Proin ut nunc a diam</div><div class="btn">Details</div></div>
  <div class="abs card" style="left:869px;top:2358px"><div class="card-img" role="img" aria-label="Laptop on a white desk" style="background:linear-gradient(180deg,#f1f2f4,#d7d9dc 70%,#b9bcc0)"></div><div class="card-title">Vivamus Pharetra</div><div class="card-desc">Donec vel tortor sed lectus laoreet hendrerit. Proin ut nunc a diam</div><div class="btn">Details</div></div>

  <div class="abs load-more">Load More</div>
</section>

<!-- contact -->
<section>
  <div class="abs map" role="img" aria-label="Street map showing the venue location"></div>
  <div class="abs contact-panel"></div>
  <h2 class="abs contact-title">Contact Us</h2>
  <div class="abs contact-line" style="top:2960px"><svg width="14" height="18" viewBox="0 0 14 18" style="margin-top:3px"><path d="M7 17S1 10.5 1 6.5a6 6 0 0112 0C13 10.5 7 17 7 17z" fill="#fff"/><circle cx="7" cy="6.5" r="2.2" fill="var(--blue)"/></svg><span>22 Harbor Lane,<br>Westfield Commons</span></div>
  <div class="abs contact-line" style="top:3025px"><svg width="14" height="16" viewBox="0 0 14 16" style="margin-top:6px"><path d="M3 1l3 3-2 2c1 2 3 4 5 5l2-2 3 3-2 3C7 15 0 8 1 3z" fill="#fff"/></svg><span>(01) 555-0147</span></div>
  <div class="abs follow">Follow Us</div>
  <div class="abs social" style="left:94px;top:3107px" role="img" aria-label="linkwave profile"></div>
  <div class="abs social" style="left:136px;top:3107px" role="img" aria-label="social profile"></div>
</section>

<!-- footer -->
<footer>
  <div class="abs footer"></div>
  <div class="abs logo foot-logo">Logo Goes Here</div>
  <div class="abs foot-small" style="left:94px;top:3377px;display:flex;gap:8px"><svg width="12" height="16" viewBox="0 0 14 18"><path d="M7 17S1 10.5 1 6.5a6 6 0 0112 0C13 10.5 7 17 7 17z" fill="var(--blue)"/></svg><span>22 Harbor Lane,<br>Westfield Commons</span></div>
  <div class="abs foot-small" style="left:94px;top:3425px;display:flex;gap:8px"><svg width="12" height="14" viewBox="0 0 14 16"><path d="M3 1l3 3-2 2c1 2 3 4 5 5l2-2 3 3-2 3C7 15 0 8 1 3z" fill="var(--blue)"/></svg><span>(01) 555-0147</span></div>
  <div class="abs social" style="left:94px;top:3460px;width:28px;height:28px" role="img" aria-label="linkwave profile"></div>
  <div class="abs social" style="left:131px;top:3460px;width:28px;height:28px" role="img" aria-label="social profile"></div>

  <div class="abs foot-head" style="left:328px">Quick Links</div>
  <div class="abs foot-link" style="left:328px;top:3377px">About Us</div>
  <div class="abs foot-link" style="left:328px;top:3405px">Auction Listing</div>
  <div class="abs foot-link" style="left:328px;top:3433px">Event Details</div>
  <div class="abs foot-link" style="left:328px;top:3462px">Contact Us</div>

  <div class="abs foot-head" style="left:517px">Support</div>
  <div class="abs foot-link" style="left:517px;top:3377px">Register</div>
  <div class="abs foot-link" style="left:517px;top:3405px">Login</div>
  <div class="abs foot-link" style="left:517px;top:3433px">User Guide</div>

  <div class="abs foot-head" style="left:672px">Event Details</div>
  <div class="abs foot-small" style="left:672px;top:3377px">Feb. 02, 2020</div>
  <div class="abs foot-strong" style="left:672px;top:3392px">Lorem ipsum dolor</div>
  <div class="abs foot-small" style="left:672px;top:3428px">Feb. 08, 2020</div>
  <div class="abs foot-strong" style="left:672px;top:3443px">Donec volutpat</div>

  <div class="abs foot-head" style="left:863px">Newsletter</div>
  <div class="abs foot-small" style="left:863px;top:3366px;font-size:12.5px">Subscribe our newsletter</div>
  <div class="abs news-input"><svg width="12" height="9" viewBox="0 0 12 9" fill="none" stroke="#999"><rect x=".5" y=".5" width="11" height="8"/><path d="M.5.5l5.5 4 5.5-4"/></svg>Enter your email id</div>
  <div class="btn subscribe">Subscribe</div>

  <div class="abs foot-rule"></div>
  <div class="abs copyright">© 2020 <span>Logo Goes Here</span>. All Rights Reserved.</div>
</footer>

<!-- login modal -->
<div class="abs dim"></div>
<div class="abs modal" role="dialog" aria-label="Login to bid">
  <svg class="modal-close" width="22" height="22" viewBox="0 0 22 22" stroke="#222" stroke-width="1.6"><path d="M2 2l18 18M20 2L2 20"/></svg>
  <div class="modal-title">To Place a Bid please login</div>
  <div class="field" style="top:100px">Name</div>
  <div class="field" style="top:149px">Email id</div>
  <div class="btn">Login Now</div>
</div>

</body>
</html>
```